Business card

Looking for modern clean business card off logo below. Very important to be clean and professional but want fun as well

Industry/Entity Type

Business

```html
<!DOCTYPE html>
<html lang="en">
<head>
<meta charset="utf-8">
<title>Crestline Estates – Business Card</title>
<link rel="stylesheet" href="https://fonts.googleapis.com/css2?family=Oswald:wght@500&family=Jost:wght@400&display=swap">
<style>
  :root {
    --bg: #f2f2f3;
    --sky: #5cb0d1;
    --slate: #5d5d5d;
    --ink: #111111;
    --paper: #ffffff;
    --brand-text: #575757;
  }
  html, body {
    margin: 0;
    padding: 0;
    width: 1200px;
    height: 1000px;
    overflow: hidden;
    background: var(--bg);
  }
  .canvas {
    position: relative;
    width: 1200px;
    height: 1000px;
  }
  .card {
    position: absolute;
    left: 305px;
    width: 599px;
    height: 342px;
    background: var(--paper);
    overflow: hidden;
  }
  .card--front { top: 158px; }
  .card--back { top: 571px; width: 598px; }

  .band { position: absolute; left: 0; width: 100%; }
  .band--top { top: 0; height: 138px; background: var(--sky); }
  .band--middle { top: 138px; height: 71px; background: var(--paper); }
  .band--bottom { top: 209px; height: 133px; background: var(--slate); }

  .brand-dot {
    position: absolute;
    left: 100px;
    top: 118px;
    width: 104px;
    height: 104px;
    border-radius: 50%;
    background: var(--paper);
  }
  .brand-name {
    position: absolute;
    left: 213px;
    top: 140px;
    margin: 0;
    font-family: "Oswald", sans-serif;
    font-weight: 500;
    font-size: 44px;
    line-height: 52px;
    letter-spacing: 0.5px;
    color: var(--brand-text);
    text-transform: uppercase;
    white-space: nowrap;
  }
  .brand-tagline {
    position: absolute;
    left: 217px;
    top: 190px;
    margin: 0;
    font-family: "Jost", sans-serif;
    font-size: 13px;
    line-height: 14px;
    color: var(--brand-text);
    white-space: nowrap;
  }

  .back-mark {
    position: absolute;
    left: 464px;
    top: 50px;
    width: 70px;
    text-align: center;
  }
  .back-mark__dot {
    display: block;
    width: 38px;
    height: 38px;
    margin: 0 auto 6px;
    border-radius: 50%;
    background: var(--sky);
  }
  .back-mark__name {
    font-family: "Jost", sans-serif;
    font-size: 9px;
    line-height: 11px;
    color: var(--brand-text);
    text-transform: uppercase;
    letter-spacing: 0.5px;
  }

  .contact-list {
    position: absolute;
    left: 91px;
    top: 109px;
    margin: 0;
    padding: 0;
    list-style: none;
    font-family: "Jost", sans-serif;
    font-size: 22px;
    line-height: 28.6px;
    color: var(--ink);
  }
</style>
</head>
<body>
<main class="canvas">
  <section class="card card--front" aria-label="Business card front">
    <div class="band band--top"></div>
    <div class="band band--middle"></div>
    <div class="band band--bottom"></div>
    <span class="brand-dot" aria-hidden="true"></span>
    <h1 class="brand-name">Crestline Estates</h1>
    <p class="brand-tagline">Property Management and Real Estate</p>
  </section>

  <section class="card card--back" aria-label="Business card back">
    <div class="back-mark">
      <span class="back-mark__dot" aria-hidden="true"></span>
      <span class="back-mark__name">Crestline Estates</span>
    </div>
    <ul class="contact-list">
      <li>name</li>
      <li>cell</li>
      <li>fax</li>
      <li>email</li>
      <li>web</li>
    </ul>
  </section>
</main>
</body>
</html>
```